依頼詳細
★重視する点
60歳~70歳の社長が読むものです。
商品も50万円以上のコンサルティングなので、
信頼感、安心感を与える雰囲気を重視します。
また、高級感のあるイメージも重要です。

★ページ構成について
表面 キャッチ
中面 スキームの説明、Q&A
裏面 報酬、お問合せ先

内容を詰めることができれば、
A4裏表の1枚でもOKです。
(むしろ、そうできればベストです)

★文章の修正について
必要があれば文章やタイトルの修正もOKです。
目的は、
「このような方法があるなら、もっと話しを聞いてみたい」
と思わせることです。
そのように思わせるものであれば、
タイトルや文章の修正も歓迎します。

★お問合せの部分について
数名でこのパンフを共同利用する予定です。
ですから、お問合せの部分は
各自の住所と会社名、電話番号、メールアドレスなどが
入りますので、そのようなスペースを空けておいてください。

★利用用途
このパンフレットは、
問合せがあった人に、最初の相談の時、お渡しします。
またセミナーなど開催したときに、資料としてお渡しします。

★納品形式について
イラストレーターV14で開ける形式でお願いいたします。
また、JpegやPNGもお願いします。
サイズ
A4
ページ数
4ページ
希望イメージ
シンプル 複雑
単色 カラフル
暗い 明るい
日常 高級
遊び心 厳粛
未来的 伝統的
女性的 男性的
希望する色
茶系、グレー系
納品ファイル
• 高解像度JPG (.jpg)
• イラストレーター形式 (.ai)
• PNG形式 (.png)
補足説明
・表面、中面、裏面のラフ案をご提案ください。
こちらの希望するイメージに近い提案を1つ選択させて頂きます。

・希望に近づけるために、修正要望を個別にさせていただくこともあります。
コンペ方式のため、修正後に当選されない場合も、どうかご了承ください。
参加報酬は4件用意していますので、
なるべくそちらで対応するようにいたします。

・今後も同様なものを作成する予定です。
依頼は今回だけではなく、こちらの求める条件に合えば
継続して依頼したいと思います。

・疑問点などございましたらお気軽にご質問ください。
早速に1件のご提案があり、大変ありがとうございます。
さすがプロの方のデザインはすばらしく、
これからの提案もとても期待しております。

★お願い スキームの図解もデザインに盛り込んでください

原案に、自社株信託のスキームの図解がありますが、
できれば、パンフレットにも図解を盛り込んで
いただけないでしょうか?
もちろん、原案のスキームの図を参考に
あなたのイメージするようにデザインし直していただきたいです。

原案がワードで作成したため、マクロウィルスなどご心配の方も
いらっしゃると思いますので、原案のPDFを添付します。
また、スキームの図のPNGも添付します。
図はMSのVisioというソフトで作っております。
開ける人は少ないでしょうが、そのファイルも添付します。
■ 選んだ理由

ビジネスというジャングルを駆け巡る獅子(社長)が
寂しげな目で「引退するか」という表紙は、
提案の中で、圧倒的でした。

また、多くの提案をいただいて、気づいたのですが、
老夫婦だと保険の勧誘、引退をイメージする物だと
投資信託などの金融商品の勧誘のような印象を与えることがわかり、
ライオンの表紙はそのような印象も与えないので、
当選とさせていただきました。

■ 提案者全員のお礼・コメント

多くの方からご応募いただき、誠にありがとうございました。
どの提案も、とても私のような素人ではできない
優れたデザインだったと思います。
さすがプロの仕事を見せていただきました。
また、今後も提案をお願いすると思いますが、
そのときも、よろしくお願いいたします。

この度は大変ありがとうございました。

```html
<!DOCTYPE html>
<html lang="ja">
<head>
<meta charset="utf-8">
<title>自社株信託のご案内</title>
<link rel="stylesheet" href="https://fonts.googleapis.com/css2?family=Noto+Sans+JP:wght@400;500;700&display=swap">
<style>
:root{
  --brown:#9a5a2c;
  --brown-dark:#6e3f1e;
  --accent:#c8741f;
  --ink:#3a3a3a;
  --muted:#777;
  --band:#e7e3de;
  --line:#cfc8c0;
  --paper:#ffffff;
}
*{margin:0;padding:0;box-sizing:border-box}
html,body{width:849px;height:1200px;overflow:hidden;background:var(--paper)}
body{font-family:"Noto Sans JP",sans-serif;color:var(--ink);font-size:9px;line-height:1.5;position:relative}
.headline{position:absolute;left:22px;top:14px;font-size:28px;font-weight:700;color:var(--accent);letter-spacing:.02em}
.headline strong{color:var(--brown-dark)}
.headline-rule{position:absolute;left:22px;right:22px;top:58px;height:2px;background:var(--brown)}
.qa{position:absolute;left:22px;right:22px;top:70px;display:grid;grid-template-columns:1fr 1fr;column-gap:12px;row-gap:8px}
.card{border-top:1px solid var(--line)}
.card-head{background:var(--band);padding:3px 8px;font-weight:700;font-size:10.5px;color:var(--ink)}
.card-head .mark{color:var(--accent);font-size:12px;margin-right:6px}
.card-body{padding:5px 8px;min-height:52px}
.section-title{position:absolute;left:22px;font-weight:700;font-size:11px;color:var(--brown)}
.scheme{position:absolute;left:22px;top:528px;width:805px;height:88px}
.points{position:absolute;left:22px;top:640px;width:520px}
.points li{list-style:none;padding-left:12px;position:relative;margin-bottom:3px}
.points li::before{content:"";position:absolute;left:0;top:4px;width:6px;height:6px;background:var(--brown)}
.photo{position:absolute;left:560px;top:622px;width:268px;height:180px;background:radial-gradient(circle at 50% 45%,#fbfaf7 0%,#ece7e0 60%,#d9d2c8 100%)}
.bubble{position:absolute;left:700px;top:630px;width:118px;height:70px;border-radius:50%;border:1px solid var(--line);background:#fff;display:flex;align-items:center;justify-content:center;text-align:center;font-size:10px;font-weight:500}
.fee{position:absolute;left:22px;top:836px;width:805px}
.note{color:var(--muted);font-size:7.5px;margin-top:4px}
.contact-title{position:absolute;left:22px;top:905px;font-weight:700;font-size:10px;color:var(--ink)}
</style>
</head>
<body>
<h1 class="headline">生前贈与でも、遺言でもない<strong>「自社株信託」</strong></h1>
<div class="headline-rule"></div>

<section class="qa">
  <div class="card"><div class="card-head"><span class="mark">Q</span>贈与税はかからないか？</div>
    <div class="card-body">株を後継者に渡すと贈与税が心配です。評価額が高い場合、多額の税負担が生じます。例えば3000万円なら1200万円以上の贈与税が必要ですか？</div></div>
  <div class="card"><div class="card-head"><span class="mark">A</span>自社株信託の契約があれば</div>
    <div class="card-body">贈与税がかからないように契約が可能です。この場合でも、入棄権は後継者に移転させることができます。</div></div>

  <div class="card"><div class="card-head"><span class="mark">Q</span>受託者として信託銀行などが必要になるのではないか？</div>
    <div class="card-body">「信託」として受託者は信託銀行や信託会社でなければならないと聞きます。費用も高額になるのではないでしょうか？</div></div>
  <div class="card"><div class="card-head"><span class="mark">A</span>自社株信託の契約があれば</div>
    <div class="card-body">「受託者」を後継者とすることで、許可のある信託銀行などは必要ありません。専門家の費用のみで実行できます。</div></div>

  <div class="card"><div class="card-head"><span class="mark">Q</span>オーナーへの相続が発生したらどうなるのか？</div>
    <div class="card-body">遺言がなければ、株の相続人全員で遺産分割協議が必要です。協議がまとまらず、会社の経営に支障が出ることもあります。</div></div>
  <div class="card"><div class="card-head"><span class="mark">A</span>自社株信託の契約があれば</div>
    <div class="card-body">自分の死亡の後の受益者を決めておくことで、オーナーが亡くなっても遺産分割協議は不要です。経営は安定して継続します。</div></div>

  <div class="card"><div class="card-head"><span class="mark">Q</span>後継者に株を渡した後、後継者が会社を辞めることになったら？</div>
    <div class="card-body">株を渡した後で後継者が辞めた場合、株を取り戻すのは難しく、買い取りの費用も必要になります。</div></div>
  <div class="card"><div class="card-head"><span class="mark">A</span>自社株信託の契約があれば</div>
    <div class="card-body">信託を終了させることで、議決権をオーナーに戻すことができます。費用負担もなく、柔軟に対応できます。</div></div>

  <div class="card"><div class="card-head"><span class="mark">Q</span>後継者がまだ若く、経営を任せるのが不安では？</div>
    <div class="card-body">経験の浅い後継者にすべてを任せるのは心配です。もう少し見守りながら承継を進めたいのですが。</div></div>
  <div class="card"><div class="card-head"><span class="mark">A</span>自社株信託の契約があれば</div>
    <div class="card-body">オーナーが指図権を持つことで、経営への関与を続けながら、段階的に承継を進めることができます。</div></div>
</section>

<div class="section-title" style="top:510px">自社株信託のスキーム</div>
<svg class="scheme" viewBox="0 0 805 88" aria-label="自社株信託のスキーム図">
  <g font-size="9" fill="#3a3a3a" font-family="Noto Sans JP, sans-serif">
    <rect x="0" y="30" width="70" height="28" fill="#e7e3de"/><text x="35" y="48" text-anchor="middle">委託者</text>
    <rect x="150" y="4" width="90" height="28" fill="#e7e3de"/><text x="195" y="22" text-anchor="middle">受託者（後継者）</text>
    <rect x="150" y="56" width="90" height="28" fill="#e7e3de"/><text x="195" y="74" text-anchor="middle">受益者（オーナー）</text>
    <rect x="300" y="30" width="80" height="28" fill="#9a5a2c"/><text x="340" y="48" text-anchor="middle" fill="#fff">会社</text>
    <path d="M70 44 L150 18 M70 44 L150 70 M240 18 L300 44" stroke="#9a5a2c" stroke-width="1.5" fill="none"/>
    <text x="270" y="26" font-size="8">議決権</text>
    <rect x="425" y="30" width="70" height="28" fill="#e7e3de"/><text x="460" y="48" text-anchor="middle">オーナー</text>
    <rect x="575" y="4" width="90" height="28" fill="#e7e3de"/><text x="620" y="22" text-anchor="middle">受託者</text>
    <rect x="575" y="56" width="90" height="28" fill="#e7e3de"/><text x="620" y="74" text-anchor="middle">相続後の受益者</text>
    <rect x="725" y="30" width="80" height="28" fill="#9a5a2c"/><text x="765" y="48" text-anchor="middle" fill="#fff">会社</text>
    <path d="M495 44 L575 18 M495 44 L575 70 M665 18 L725 44" stroke="#9a5a2c" stroke-width="1.5" fill="none"/>
  </g>
</svg>

<div class="section-title" style="top:624px">自社株信託のポイント</div>
<ul class="points">
  <li>自社株信託のスキームを使えば、オーナーが生前に議決権を後継者に移し、経営を任せることができます。</li>
  <li>この際、贈与税がかかる贈与ではなく、信託という形で株を移すため、税負担を抑えられます。</li>
  <li>オーナーは受益者として配当などを受け取り、生活の安定を確保できます。</li>
  <li>オーナーの相続発生時も、遺産分割協議なしに後継者へ円滑に承継されます。</li>
  <li>後継者が辞めた場合など、信託を終了させて議決権を戻すことも可能です。</li>
  <li>信託契約書の作成は、専門家が「信託監督人」や「受益者代理人」として関与します。</li>
</ul>
<div class="photo" role="img" aria-label="白い小型犬の写真"></div>
<div class="bubble">一緒に話を聞いて<br>みませんか、ワン！</div>

<div class="section-title" style="top:818px">自社株信託 報酬</div>
<div class="fee">
  <p>信託契約作成：基本50万円プラス株式の評価額で加算（税別）、信託内容変更：報酬10万円（税別）。</p>
  <p>受益者代理人：月3万円（税別）、信託監督人：月1万円（税別）</p>
  <p class="note">※報酬は会社の規模や株式の状況により異なります。詳しくはお問合せください。</p>
</div>

<div class="contact-title">お問合せ先</div>
</body>
</html>
```